New Poster Design Project

Make an out standing A2 poster with below information,it is out first edition!Use the Attached image as background,Thanx!

Tolvik Meridian Arts Gathering
16 - 22 June 2014
Www.tmagfest.example

Creating a new vision of Africa through African Arts and Culture

Guest speakers / Artists

Delphine Korrato-Væstrup (S.A)
Tekle Berhanu Woldesan (Ethio)
Ronny Bastien-Kolo (Uganda)
Håkon Lunde (Nor)
Velvet Drum Collective (Zim)
Kalumbero Band (Moz,Nor,Swe & Zim)
Dj Zoto Zoto with Afro beats (Ghana/UK )
Dj Marquee/Storm Duchess with collage mix (Bergen)

@ Cafe Lutembe, Nordvik Global Heritage House (Nghh) Helsebrygga,Kjøpmannsplassen,Lindehagen & Vevergangen gate

Mon-Thur
Free entry,food & drinks served

Fri - Entry by donation & Sat - Tmagfest closing ceremony (100kr)
Updates

Project Deadline Extended

Project Deadline Extended
Reason: I made a mistake on extending time on this project now I can not reverse the extended time aaarrrr!!!I really dont have time,The poster should be all over the place by now since Im left with a couple of days away to the festival!!!I need someone to QuickFix me a A2 top notch poster in No time...my deadline is NOW NOW,LATEST Wednesday 21 May 2014,Thanx!

Industry/Entity Type

Cafe

Requirements
Must have
• sponsors logo
Nice to have
• Symbols
Should not have

```html
<!DOCTYPE html>
<html lang="en">
<head>
<meta charset="utf-8">
<title>Tolvik Meridian Arts Gathering</title>
<link rel="stylesheet" href="https://fonts.googleapis.com/css2?family=Cinzel:wght@700;900&display=swap">
<style>
  :root {
    --paper: #ffffff;
    --bracket: #9a9a9a;
    --mustard: #c4b71c;
    --mustard-deep: #a89b12;
    --crimson: #c9271d;
    --crimson-deep: #9c1a13;
    --rust: #a9591b;
    --rust-deep: #7d3f12;
    --white: #ffffff;
    --gold-text: #d8b41e;
    --orange-text: #e0861d;
    --ink: #111111;
    --sponsor: #555555;
  }
  * { margin: 0; padding: 0; box-sizing: border-box; }
  html, body { width: 1000px; height: 1200px; overflow: hidden; background: var(--paper); }
  body { font-family: "Cinzel", "Times New Roman", serif; font-weight: 700; position: relative; }

  .bracket { position: absolute; background: var(--bracket); }

  .hero {
    position: absolute; left: 106px; top: 50px; width: 756px; height: 505px;
    background: radial-gradient(ellipse at 55% 40%, #d3c636 0%, var(--mustard) 45%, var(--mustard-deep) 100%);
  }
  .hero-title {
    position: absolute; left: 0; top: 4px; width: 100%; text-align: center;
    color: var(--white); font-size: 66px; line-height: 105px; letter-spacing: 2px; font-weight: 900;
  }
  .hero-dates {
    position: absolute; left: 0; top: 204px; width: 100%; text-align: center;
    color: var(--white); font-size: 46px; letter-spacing: 1px; font-weight: 900;
  }
  .hero-tagline {
    position: absolute; left: 0; top: 316px; width: 100%; text-align: center;
    color: var(--white); font-size: 30px; line-height: 46px;
  }
  .symbol-strip {
    position: absolute; left: 291px; top: 418px; width: 172px; height: 44px; background: var(--white);
  }

  .lineup {
    position: absolute; left: 108px; top: 555px; width: 422px; height: 447px;
    background: linear-gradient(135deg, var(--crimson) 0%, #c3271f 55%, var(--crimson-deep) 100%);
    color: var(--white); padding: 22px 12px 0 13px;
  }
  .lineup-heading { font-size: 33px; line-height: 42px; }
  .lineup-heading .arrow { vertical-align: middle; margin-left: 10px; }
  .lineup-list { font-size: 22.5px; line-height: 28px; margin-top: 4px; }

  .venues {
    position: absolute; left: 550px; top: 568px; width: 312px; height: 207px;
    background: linear-gradient(135deg, var(--rust) 0%, var(--rust-deep) 100%);
    color: var(--white); text-align: right; font-size: 19.5px; line-height: 27.5px;
    padding: 16px 14px 0 10px;
  }

  .entry {
    position: absolute; left: 540px; width: 304px; text-align: right;
    font-size: 19.5px; line-height: 27px;
  }
  .entry-free { top: 806px; color: var(--gold-text); }
  .entry-weekend { top: 886px; color: var(--orange-text); }

  .site {
    position: absolute; left: 250px; top: 1040px; width: 476px; text-align: center;
    color: var(--ink); font-size: 27px; font-weight: 900;
  }

  .sponsors {
    position: absolute; left: 104px; top: 1102px; width: 576px; height: 58px;
    display: grid; grid-template-columns: repeat(6, 1fr); column-gap: 8px; align-items: center;
  }
  .sponsor {
    display: flex; align-items: center; justify-content: center; gap: 4px;
    color: var(--sponsor); font-size: 11px; line-height: 13px; text-align: center;
  }
  .sponsor .dot { flex: none; width: 12px; height: 12px; border-radius: 50%; background: var(--sponsor); }

  .client-mark {
    position: absolute; left: 692px; top: 1056px; width: 186px; height: 116px;
    background: var(--paper); border: 1px solid #e4e4e4;
    display: flex; align-items: center; justify-content: center; gap: 8px;
    color: var(--ink); font-size: 28px; letter-spacing: 6px;
  }
  .client-mark .square { width: 20px; height: 20px; background: var(--ink); }
</style>
</head>
<body>
  <div class="bracket" style="left:60px;top:0;width:6px;height:100px"></div>
  <div class="bracket" style="left:60px;top:0;width:112px;height:5px"></div>
  <div class="bracket" style="left:908px;top:0;width:6px;height:100px"></div>
  <div class="bracket" style="left:828px;top:0;width:86px;height:5px"></div>
  <div class="bracket" style="left:60px;top:1080px;width:6px;height:120px"></div>
  <div class="bracket" style="left:60px;top:1195px;width:112px;height:5px"></div>
  <div class="bracket" style="left:908px;top:1080px;width:6px;height:120px"></div>
  <div class="bracket" style="left:828px;top:1195px;width:86px;height:5px"></div>

  <section class="hero" role="img" aria-label="Yellow-toned photograph of a smiling woman wearing a head wrap">
    <h1 class="hero-title">Tolvik Meridian<br>Arts Gathering</h1>
    <p class="hero-dates">16 - 22 June 2014</p>
    <p class="hero-tagline">Creating a new vision of Africa<br>through African Arts and Culture</p>
    <div class="symbol-strip" role="img" aria-label="Row of four adinkra symbols"></div>
  </section>

  <section class="lineup" role="img" aria-label="Red-toned photograph of a thumb piano and drum">
    <h2 class="lineup-heading">Guest speakers /<br>Artists
      <svg class="arrow" width="120" height="26" viewBox="0 0 120 26" aria-hidden="true">
        <g fill="none" stroke="#ffffff" stroke-width="3">
          <line x1="4" y1="13" x2="112" y2="13"/>
          <polyline points="4,4 12,13 4,22"/>
          <polyline points="14,4 22,13 14,22"/>
          <polyline points="24,4 32,13 24,22"/>
        </g>
        <polygon points="104,4 118,13 104,22" fill="#ffffff"/>
      </svg>
    </h2>
    <p class="lineup-list">Delphine Korrato-Væstrup (S.A) / Tekle Berhanu Woldesan (Ethio) / Ronny Bastien-Kolo (Uganda) / Håkon Lunde (Nor) / Velvet Drum Collective (Zim) / Kalumbero Band (Moz,Nor,Swe &amp; Zim) / Dj Zoto Zoto with Afro beats (Ghana/UK ) / Dj Marquee/Storm Duchess with collage mix (Bergen)</p>
  </section>

  <section class="venues" role="img" aria-label="Brown-toned photograph of a drum">
    <p>@ Cafe Lutembe, Nordvik Global Heritage House (Nghh) Helsebrygga, Kjøpmannsplassen, Lindehagen &amp; Vevergangen gate</p>
  </section>

  <p class="entry entry-free">Mon-Thur Free entry,<br>food &amp; drinks served</p>
  <p class="entry entry-weekend">Fri - Entry by donation<br>&amp; Sat - Tmagfest closing<br>ceremony (100kr)</p>

  <p class="site">Www.tmagfest.example</p>

  <div class="sponsors">
    <span class="sponsor"><span class="dot"></span>Kanja Dance Troupe</span>
    <span class="sponsor">Fundra</span>
    <span class="sponsor">Kraftstua</span>
    <span class="sponsor">Tolvik Kommune</span>
    <span class="sponsor">Dugnadsnett</span>
    <span class="sponsor">Nordvik Global Heritage House</span>
  </div>

  <div class="client-mark"><span class="square"></span>TMAG</div>
</body>
</html>
```